タイトル 「週末ガーデナーのための水やり流・花咲かせ節約術」
サブタイトル 「毎日が楽になる5つの習慣」

上記の表紙デザインをお願いします。基本お任せします。
本の内容  原稿を添付します。

その他ご不明な点がございましたらお気楽にご質問ください。よろしくお願いいたします。
著者名 星空ナビゲーター 森川佳代 from神戸

本の内容とよくマッチしたデザインだと思いました。インパクトもあり本の対象であるアラフォーの好みと合っているように思いました。

沢山のご応募ありがとうございました。何もかもか初めての作業で、不安でしたが、関心を持っていただいて心からありがたく思っております。これからも電子書籍の出版を考えております。ご縁がありましたらまた、今後もよろしくお願いします。
ありがとうございました。

```html
<!DOCTYPE html>
<html lang="ja">
<head>
<meta charset="utf-8">
<title>週末ガーデナーのための水やり流・花咲かせ節約術</title>
<link rel="stylesheet" href="https://fonts.googleapis.com/css2?family=M+PLUS+Rounded+1c:wght@500;800&family=Noto+Serif+JP:wght@900&family=Noto+Sans+JP:wght@500;700&display=swap">
<style>
  :root {
    --pink-bg: #e9437f;
    --pink-bg-light: #f37aa5;
    --pink-title: #e5508a;
    --magenta: #dd2577;
    --pale-pink: #fbd3e2;
    --white: #ffffff;
    --dark: #3a2a30;
  }
  * { margin: 0; padding: 0; box-sizing: border-box; }
  html, body { width: 750px; height: 1200px; overflow: hidden; }
  body { background: var(--white); }
  .cover {
    position: relative;
    width: 750px;
    height: 1200px;
    overflow: hidden;
  }
  .cover-pattern {
    position: absolute;
    inset: 0;
    background: radial-gradient(circle at 50% 40%, var(--pink-bg-light) 0%, var(--pink-bg) 70%);
  }
  .title-disc {
    position: absolute;
    left: 28px;
    top: 128px;
    width: 694px;
    height: 694px;
    border-radius: 50%;
    background: var(--white);
    box-shadow: 0 0 0 10px rgba(255,255,255,0.35), 0 0 30px rgba(180,20,80,0.35);
  }
  .disc-icons {
    position: absolute;
    inset: 18px;
    border-radius: 50%;
    background: radial-gradient(circle, transparent 0%, transparent 44%, var(--pale-pink) 58%, rgba(251,211,226,0.55) 80%, transparent 100%);
  }
  .title-block {
    position: absolute;
    left: 0;
    right: 0;
    top: 230px;
    text-align: center;
    font-family: "M PLUS Rounded 1c", sans-serif;
    font-weight: 800;
    color: var(--pink-title);
  }
  .title-lead { font-size: 40px; letter-spacing: 1px; line-height: 1.2; }
  .title-mid { font-size: 50px; letter-spacing: 1px; line-height: 1.3; margin-top: 8px; }
  .title-main {
    font-size: 112px;
    color: var(--magenta);
    letter-spacing: 8px;
    line-height: 1.2;
    margin-top: 6px;
  }
  .subtitle {
    position: absolute;
    left: 0;
    right: 0;
    top: 850px;
    text-align: center;
    font-family: "Noto Serif JP", serif;
    font-weight: 900;
    font-size: 48px;
    color: var(--white);
    letter-spacing: 2px;
    text-shadow: 0 2px 6px rgba(150,0,60,0.4);
  }
  .subtitle .num { font-size: 70px; }
  .author {
    position: absolute;
    left: 0;
    right: 0;
    top: 995px;
    text-align: center;
    font-family: "Noto Sans JP", sans-serif;
    color: var(--white);
  }
  .author-role { font-size: 28px; font-weight: 700; letter-spacing: 2px; }
  .author-name { font-size: 46px; font-weight: 700; letter-spacing: 10px; margin-top: 4px; }
  .author-from { font-size: 24px; font-weight: 500; margin-top: 2px; }
</style>
</head>
<body>
  <main class="cover">
    <div class="cover-pattern" role="img" aria-label="ピンクのハート柄の背景"></div>
    <div class="title-disc">
      <div class="disc-icons" role="img" aria-label="手紙・ハート・リボン・スマートフォン・グラスなどのピンクのアイコンイラストの輪"></div>
    </div>
    <h1 class="title-block">
      <span class="title-lead" style="display:block">週末ガーデナーのための</span>
      <span class="title-mid" style="display:block">水やり流・花咲かせ</span>
      <span class="title-main" style="display:block">節約術</span>
    </h1>
    <p class="subtitle">毎日が楽になる<span class="num">5</span>つの習慣</p>
    <div class="author">
      <p class="author-role">星空ナビゲーター</p>
      <p class="author-name">森川 佳代</p>
      <p class="author-from">from 神戸</p>
    </div>
  </main>
</body>
</html>
```